School Communication Email Template

Looking for a designer to create a couple simple email templates that are matching our brand colors and feel. Attached is the default email template that is currently being sent out. Company details can be shared upon request.

Template is to be used within the booking tool we use (snapshot below) and gmail. Template code is in HTML (see screenshot below).
Updates

Template code for website should be in HTML. Sorry if that created confusion.

Target Market(s)

Parents of kids enrolled in our classes

Industry/Entity Type

Kids sport classes

Font styles to use
Serif

Colors
0054AA
0677BA
7BADD7
CADEEF
E8F1F8
FFF300
FFF600
FEFA6F
FFFEC7
FFFEE8

Requirements
Must have
• Consistency with company brand/colors
Nice to have
• Flexibility to be adjusted as needed

```html
<!DOCTYPE html>
<html lang="en">
<head>
<meta charset="utf-8">
<title>Booking Confirmed</title>
<link rel="stylesheet" href="https://fonts.googleapis.com/css2?family=Roboto:wght@400;500;700&family=Tinos:wght@700&display=swap">
<style>
  :root {
    --brand-blue: #0054AA;
    --mid-blue: #0677BA;
    --soft-blue: #7BADD7;
    --pale-blue: #E8F1F8;
    --field-border: #a9c8e6;
    --navy: #243c84;
    --gold: #f5b21c;
    --yellow: #FFF300;
    --header-grey: #e0e0e0;
    --text: #333333;
    --muted: #444444;
    --frame: #b8c4dc;
    --white: #ffffff;
  }
  * { margin: 0; padding: 0; box-sizing: border-box; }
  html, body { width: 1200px; height: 3039px; overflow: hidden; background: var(--white); }
  body { font-family: "Roboto", Arial, sans-serif; color: var(--text); }
  .email { position: relative; width: 1200px; height: 3039px; }
  .abs { position: absolute; left: 0; width: 100%; text-align: center; }

  .masthead { position: absolute; top: 0; left: 0; width: 1200px; height: 314px; background: var(--header-grey);
    display: flex; align-items: center; justify-content: center; }
  .brand-name { font-family: "Roboto", Arial, sans-serif; font-weight: 700; font-size: 54px; color: var(--navy); }

  .title { top: 372px; font-family: "Tinos", "Times New Roman", serif; font-weight: 700; font-size: 66px; color: var(--navy); line-height: 76px; }
  .subtitle { top: 472px; font-size: 30px; color: #111; line-height: 38px; }
  .divider { position: absolute; top: 540px; left: 537px; width: 126px; height: 11px; background: var(--navy); }

  .greeting { top: 646px; font-size: 30px; line-height: 38px; }
  .recipient { top: 703px; font-family: "Tinos", "Times New Roman", serif; font-weight: 700; font-size: 41px; color: var(--gold); line-height: 48px; }
  .intro { top: 772px; font-size: 30px; line-height: 55px; color: var(--muted); }
  .intro strong { font-weight: 700; color: var(--text); }

  .details { position: absolute; top: 945px; left: 103px; width: 997px; height: 901px; border: 3px solid var(--frame); }
  .details-heading { position: absolute; top: 21px; left: 16px; width: 960px; height: 139px; background: var(--brand-blue);
    color: var(--white); font-family: "Tinos", "Times New Roman", serif; font-weight: 700; font-size: 42px; letter-spacing: 4px;
    display: flex; align-items: center; justify-content: center; }
  .detail-row { position: absolute; left: 16px; width: 960px; height: 74px; }
  .detail-label { position: absolute; left: 0; top: 0; width: 415px; height: 74px; background: var(--mid-blue); color: var(--white);
    font-size: 28px; font-weight: 500; display: flex; align-items: center; padding-left: 16px; }
  .detail-value { position: absolute; left: 441px; top: 0; width: 517px; height: 74px; background: var(--pale-blue);
    border: 3px solid var(--field-border); font-size: 26px; display: flex; align-items: center; padding-left: 14px; color: #222; }

  .manage-note { top: 1906px; font-size: 30px; line-height: 38px; color: var(--muted); }
  .manage-button { position: absolute; top: 1986px; left: 362px; width: 480px; height: 74px; background: var(--yellow);
    border: 2px solid #d8d060; font-size: 26px; letter-spacing: 1.5px; color: #222; display: flex; align-items: center; justify-content: center; text-decoration: none; }
  .appointment-id { top: 2100px; font-size: 28px; line-height: 36px; color: var(--muted); }
  .appointment-id strong { font-weight: 500; }
  .signoff { top: 2230px; font-family: "Tinos", "Times New Roman", serif; font-weight: 700; font-size: 34px; color: #000; line-height: 40px; }
  .team { top: 2289px; font-size: 30px; font-weight: 500; color: var(--navy); line-height: 38px; }

  .footer { position: absolute; top: 2374px; left: 0; width: 1200px; height: 452px; background: var(--brand-blue); color: var(--white); text-align: center; }
  .footer-brand { position: absolute; top: 80px; width: 100%; font-size: 46px; font-weight: 700; color: var(--white); }
  .footer-line { position: absolute; width: 100%; font-size: 27px; letter-spacing: 1px; line-height: 34px; }
  .footer-line.phone { top: 265px; }
  .footer-line.web { top: 310px; }
  .footer-line.address { top: 359px; }
  .sep { margin: 0 22px; }

  .social-band { position: absolute; top: 2826px; left: 0; width: 1200px; height: 213px; background: var(--pale-blue); }
  .social-link { position: absolute; top: 52px; width: 66px; height: 66px; border-radius: 50%; background: var(--navy); }
</style>
</head>
<body>
<main class="email">
  <header class="masthead">
    <span class="brand-name">Starlet Sports</span>
  </header>

  <h1 class="abs title">Thank You!</h1>
  <p class="abs subtitle">Your Booking has been confirmed.</p>
  <div class="divider"></div>

  <p class="abs greeting">Hello</p>
  <p class="abs recipient">Mia Carter</p>
  <p class="abs intro">Your Booking confirmed with <strong>Company Name</strong>. Please<br>find the details below.</p>

  <section class="details">
    <h2 class="details-heading">BOOKING DETAILS</h2>
    <div class="detail-row" style="top:184px"><div class="detail-label">Student First Name</div><div class="detail-value">Mia</div></div>
    <div class="detail-row" style="top:272px"><div class="detail-label">Student Last Name</div><div class="detail-value">Carter</div></div>
    <div class="detail-row" style="top:361px"><div class="detail-label">Appointment Name</div><div class="detail-value">Dummy Appointment</div></div>
    <div class="detail-row" style="top:448px"><div class="detail-label">Appointment Service</div><div class="detail-value">Dummy Service</div></div>
    <div class="detail-row" style="top:536px"><div class="detail-label">Booking Start Date</div><div class="detail-value">21st Feb, 2023</div></div>
    <div class="detail-row" style="top:623px"><div class="detail-label">Booking End Date</div><div class="detail-value">23rd Feb, 2023</div></div>
    <div class="detail-row" style="top:712px"><div class="detail-label">Appointment Start Time</div><div class="detail-value">Morning 11.00 AM</div></div>
    <div class="detail-row" style="top:797px"><div class="detail-label">Appointment&nbsp; End Time</div><div class="detail-value">Afternoon : 4:30 PM</div></div>
  </section>

  <p class="abs manage-note">Manage or edit your appointment online through our portal.</p>
  <a class="manage-button" href="#">MANAGE MY APPOINTMENT</a>
  <p class="abs appointment-id"><strong>Appointmnet ID:</strong> ABCD123456</p>

  <p class="abs signoff">Thanks</p>
  <p class="abs team">Team Online Portal</p>

  <footer class="footer">
    <div class="footer-brand">Starlet Sports</div>
    <p class="footer-line phone">(555) 214-0876</p>
    <p class="footer-line web">hello@starletsports.com<span class="sep">|</span>www.starletsports.com</p>
    <p class="footer-line address">48 Maple Court, Riverton, Colorado 80412</p>
  </footer>

  <nav class="social-band" aria-label="Social links">
    <a class="social-link" href="#" style="left:465px" aria-label="Social profile one"></a>
    <a class="social-link" href="#" style="left:558px" aria-label="Social profile two"></a>
    <a class="social-link" href="#" style="left:670px" aria-label="Social profile three"></a>
  </nav>
</main>
</body>
</html>
```